Disability and mental health support work company requires business card

Specialising
Wrenfield Disability is a new QCAP service aimed toward QCAP participants with a history of criminal justice, psychosocial/mental health, intellectual, and cognitive disabilities.

Our focus
Focusing on providing core QCAP supports for community participation, daily activities and supported independent living.

Authentic
Likeminded people wanting to make a difference in participant's lives.

Our aim to provide holistic and empowering supports targeted towards creating independence and guidance for all participants and families.
Over 35 years of experience working with people that have psychosocial, intellectual, and cognitive disabilities.

Industry/Entity Type

disability and mental health

Contact Information for Business Card

logo - business name

Colors
0054AA
0677BA
7BADD7
CADEEF
E8F1F8
FFF300
FFF600
FEFA6F
FFFEC7
FFFEE8

Requirements
Must have
• want double sided business cards(wont let me change it)
Should not have
• any disability related pictures

```html
<!DOCTYPE html>
<html lang="en">
<head>
<meta charset="utf-8">
<title>Wrenfield Disability — Business Card</title>
<link href="https://fonts.googleapis.com/css2?family=Montserrat:wght@400;500;700&display=swap" rel="stylesheet">
<style>
  :root {
    --navy: #163a66;
    --navy-deep: #0f2c50;
    --gold: #e8b93a;
    --paper: #ffffff;
    --backdrop: #efefef;
    --ink-soft: #2c4a72;
  }
  * { margin: 0; padding: 0; box-sizing: border-box; }
  html, body { width: 1200px; height: 1079px; overflow: hidden; }
  body {
    background: var(--backdrop);
    font-family: "Montserrat", Arial, sans-serif;
    display: flex;
    align-items: center;
    justify-content: center;
    gap: 44px;
  }
  .card {
    width: 540px;
    height: 336px;
    position: relative;
    box-shadow: 0 6px 16px rgba(0,0,0,0.28);
    overflow: hidden;
  }
  .card--back { background: var(--navy); }
  .card--front { background: var(--paper); }

  .brand {
    position: absolute;
    display: flex;
    align-items: center;
    gap: 10px;
  }
  .brand__dot {
    width: 20px; height: 20px;
    border-radius: 50%;
    border: 2px solid var(--gold);
  }
  .brand__name {
    font-weight: 700;
    font-size: 15px;
    letter-spacing: 0.04em;
    text-transform: uppercase;
  }
  .card--back .brand { left: 40px; bottom: 92px; }
  .card--back .brand__name { color: var(--gold); }
  .card--front .brand { left: 28px; top: 30px; }
  .card--front .brand__dot { border-color: var(--navy); }
  .card--front .brand__name { color: var(--navy); font-size: 13px; }

  .sun-decoration {
    position: absolute;
    right: 0; bottom: 0;
    width: 290px; height: 250px;
    background: radial-gradient(circle at 100% 100%, var(--navy-deep) 0%, rgba(15,44,80,0.6) 45%, rgba(22,58,102,0) 75%);
  }

  .holder {
    position: absolute;
    left: 28px; bottom: 66px;
    color: var(--navy);
  }
  .holder__name { font-weight: 700; font-size: 27px; letter-spacing: 0.02em; }
  .holder__role { font-weight: 500; font-size: 17px; margin-top: 4px; letter-spacing: 0.03em; }

  .contact {
    position: absolute;
    left: 298px; bottom: 56px;
    list-style: none;
    font-size: 13px;
    color: var(--ink-soft);
    line-height: 1.55;
  }
  .contact__label { display: inline-block; width: 28px; font-weight: 700; color: var(--navy); }
</style>
</head>
<body>
  <section class="card card--back" aria-label="Card back">
    <div class="sun-decoration" role="img" aria-label="Decorative sunburst rays in deep navy"></div>
    <div class="brand">
      <span class="brand__dot"></span>
      <span class="brand__name">Wrenfield Disability</span>
    </div>
  </section>

  <section class="card card--front" aria-label="Card front">
    <div class="brand">
      <span class="brand__dot"></span>
      <span class="brand__name">Wrenfield Disability</span>
    </div>
    <div class="holder">
      <p class="holder__name">JOHN DOE</p>
      <p class="holder__role">FOUNDER</p>
    </div>
    <ul class="contact">
      <li><span class="contact__label">P :</span>+00 000 000 000</li>
      <li><span class="contact__label">E :</span>hello@wrenfieldcare.com</li>
      <li><span class="contact__label">W:</span>www.wrenfieldcare.com</li>
    </ul>
  </section>
</body>
</html>
```